Verdant Loop Advisors, LLC

I am looking for a simple, clear layout with my logo prominent and embossed, on the best quality card stock available. I would like the business name and phone number included on the card as well......I dont want my name anywhere on the card and I would like my logo embossed on the card......something simple with a white back......open to designs as long as they go along with recycling symbols and green type stuff.....The address, website, cell number, fax number, and email are listed below

5374 Tillbury Fenwood Road
Hyattsville, MD 20785

c. 240.555.0143 f. 240.555.0187
e. sales@verdantloopadvisors.example
w. www.verdantloopadvisors.example

Industry/Entity Type

Recycling

```html
<!DOCTYPE html>
<html lang="en">
<head>
<meta charset="utf-8">
<title>Verdant Loop Advisors, LLC — Business Card</title>
<link rel="stylesheet" href="https://fonts.googleapis.com/css2?family=Questrial&display=swap">
<style>
  :root {
    --backdrop: #5f5a5b;
    --card-edge: #2b2b2b;
    --card-white: #ffffff;
    --card-tint: #e6efe8;
    --brand-green: #1f7a3c;
    --label-green: #237a3f;
    --ink: #1a1a1a;
    --band: rgba(214, 226, 217, 0.55);
    --pin-red: #e0312b;
  }
  * { margin: 0; padding: 0; box-sizing: border-box; }
  html, body {
    width: 1200px; height: 1000px; overflow: hidden;
    background: var(--backdrop);
    font-family: "Questrial", "Century Gothic", sans-serif;
  }
  .card {
    position: absolute; left: 216px; top: 256px;
    width: 802px; height: 459px;
    border: 1px solid var(--card-edge);
    background: linear-gradient(135deg, var(--card-tint) 0%, var(--card-white) 45%, var(--card-white) 70%, var(--card-tint) 100%);
    overflow: hidden;
  }
  .card__accent {
    position: absolute; right: 0; top: 200px;
    width: 290px; height: 259px;
    background: linear-gradient(160deg, rgba(222,234,225,0.7), rgba(240,245,241,0.3));
  }
  .brand {
    position: absolute; left: 0; right: 0; top: 26px;
    display: flex; justify-content: center; align-items: center; gap: 18px;
  }
  .brand__mark {
    width: 74px; height: 74px; border-radius: 50%;
    background: var(--brand-green);
  }
  .brand__name {
    color: var(--ink); font-weight: 400; line-height: 1;
  }
  .brand__main { display: block; font-size: 42px; letter-spacing: 1px; }
  .brand__sub { display: block; font-size: 17px; letter-spacing: 8px; margin-top: 8px; }
  .contact { list-style: none; }
  .contact__row {
    position: absolute; left: 11px; height: 42px; width: 560px;
    display: flex; align-items: center;
    background: linear-gradient(90deg, var(--band) 0%, var(--band) 55%, rgba(214,226,217,0) 100%);
    font-size: 21px;
  }
  .contact__icon { position: absolute; left: 20px; width: 22px; height: 22px; }
  .contact__label { position: absolute; left: 54px; color: var(--label-green); }
  .contact__value { position: absolute; left: 151px; color: var(--ink); white-space: nowrap; }
</style>
</head>
<body>
  <section class="card" aria-label="Business card">
    <div class="card__accent"></div>

    <header class="brand">
      <span class="brand__mark"></span>
      <h1 class="brand__name">
        <span class="brand__main">VERDANT LOOP</span>
        <span class="brand__sub">ADVISORS, LLC</span>
      </h1>
    </header>

    <ul class="contact">
      <li class="contact__row" style="top:164px">
        <svg class="contact__icon" viewBox="0 0 24 24"><path d="M12 3a6 6 0 0 0-6 6c0 4.5 6 12 6 12s6-7.5 6-12a6 6 0 0 0-6-6zm0 8.3a2.3 2.3 0 1 1 0-4.6 2.3 2.3 0 0 1 0 4.6z" fill="var(--pin-red)"/></svg>
        <span class="contact__label">Address:</span>
        <span class="contact__value">5374 Tillbury Fenwood Road Hyattsville, MD 20785</span>
      </li>
      <li class="contact__row" style="top:221px">
        <svg class="contact__icon" viewBox="0 0 24 24"><circle cx="12" cy="12" r="10" fill="none" stroke="var(--brand-green)" stroke-width="2"/><path d="M8.5 7.5l1.8-.5 1.2 2.4-1.2 1c.6 1.3 1.6 2.3 2.9 2.9l1-1.2 2.4 1.2-.5 1.8c-3.9.3-7.9-3.7-7.6-7.6z" fill="var(--brand-green)"/></svg>
        <span class="contact__label">Phone:</span>
        <span class="contact__value">240-555-0143</span>
      </li>
      <li class="contact__row" style="top:277px">
        <svg class="contact__icon" viewBox="0 0 24 24"><rect x="7" y="3" width="10" height="5" fill="var(--brand-green)"/><rect x="3" y="9" width="18" height="8" rx="2" fill="var(--brand-green)"/><rect x="7" y="14" width="10" height="7" fill="#fff" stroke="var(--brand-green)" stroke-width="2"/></svg>
        <span class="contact__label">Fax:</span>
        <span class="contact__value" style="left:158px">(240) 555-0187</span>
      </li>
      <li class="contact__row" style="top:334px">
        <svg class="contact__icon" viewBox="0 0 24 24"><rect x="2.5" y="5.5" width="19" height="13" fill="none" stroke="var(--brand-green)" stroke-width="2"/><path d="M3 6l9 7 9-7M3 18l7-6M21 18l-7-6" fill="none" stroke="var(--brand-green)" stroke-width="2"/></svg>
        <span class="contact__label">Email:</span>
        <span class="contact__value">sales@verdantloopadvisors.example</span>
      </li>
      <li class="contact__row" style="top:392px">
        <svg class="contact__icon" viewBox="0 0 24 24"><circle cx="11" cy="11" r="8.5" fill="none" stroke="var(--brand-green)" stroke-width="2"/><path d="M2.5 11h17M11 2.5v17M5 6h12M5 16h12" stroke="var(--brand-green)" stroke-width="1.5" fill="none"/><path d="M13 13l8 3-3 1-1 3z" fill="var(--brand-green)"/></svg>
        <span class="contact__label">Website:</span>
        <span class="contact__value">www.verdantloopadvisors.example</span>
      </li>
    </ul>
  </section>
</body>
</html>
```